Brightmoor Crest Real Estate Company needs Website

I need an updated, easy to use website for my Real Estate company based out of Amarillo, TX.
Our current focus is on residential rental properties. However we are looking to expand into multi-family rentals, commercial rentals, and vacation rentals.
We also offer Real Estate Listing services.
The final design should be user friendly.

Target Market(s)

Homeowners and renters

Industry/Entity Type

Real Estate

Coding

Coded - Design and coding required

Number of Pages Required

1 page

Font styles to use
Sans Serif

Requirements
Must have
• Easy to navigate

```html
<!DOCTYPE html>
<html lang="en">
<head>
<meta charset="utf-8">
<title>Brightmoor Crest Properties</title>
<link href="https://fonts.googleapis.com/css2?family=Open+Sans:wght@400;600;700&display=swap" rel="stylesheet">
<style>
:root{
  --navy:#1f3b63;
  --blue:#5b92d3;
  --band:#79a6dc;
  --text:#555b63;
  --muted:#8a9097;
  --light:#f2f3f5;
  --line:#d9dce0;
  --footer:#2f3236;
  --footer-text:#a9adb2;
  --white:#ffffff;
}
*{margin:0;padding:0;box-sizing:border-box}
html,body{width:809px;height:1200px;overflow:hidden}
body{position:relative;background:var(--white);font-family:"Open Sans",Arial,sans-serif;color:var(--text)}

.site-header{position:absolute;top:0;left:0;width:809px;height:75px;background:var(--white)}
.brand{position:absolute;left:96px;top:24px;display:flex;align-items:center;gap:8px}
.brand-mark{width:14px;height:14px;border-radius:50%;background:var(--blue)}
.brand-name{font-size:19px;font-weight:700;color:var(--navy);letter-spacing:.2px}
.main-nav{position:absolute;right:92px;top:42px;display:flex;gap:22px;font-size:10px;color:var(--muted)}
.main-nav a{color:inherit;text-decoration:none;padding-bottom:6px}
.main-nav a.active{color:var(--blue);border-bottom:2px solid var(--blue)}

.hero{position:absolute;top:75px;left:0;width:809px;height:270px;
  background:linear-gradient(180deg,#c9d3dc 0%,#9aa6ae 35%,#5f6a6f 62%,#7d9aa8 78%,#a8c4cf 100%)}
.hero-arrow{position:absolute;top:125px;width:14px;height:20px}
.hero-arrow.prev{left:6px}.hero-arrow.next{right:6px}

.welcome{position:absolute;top:380px;left:0;width:809px;text-align:center}
.welcome h1{font-size:19px;font-weight:600;color:#3a3f45}
.welcome p{width:700px;margin:14px auto 0;font-size:7.5px;line-height:12px;color:var(--muted)}

.services{position:absolute;top:484px;left:80px;width:650px;display:flex}
.service{width:162.5px;text-align:center;padding:0 14px}
.service-icon{width:46px;height:46px;border-radius:50%;background:var(--blue);margin:0 auto;display:flex;align-items:center;justify-content:center}
.service h3{font-size:10px;font-weight:600;color:var(--blue);margin-top:12px}
.service p{font-size:7px;line-height:10.5px;color:var(--muted);margin-top:6px}

.listings{position:absolute;top:634px;left:0;width:809px;height:271px;background:var(--band)}
.listings h2{position:absolute;top:30px;width:100%;text-align:center;font-size:17px;font-weight:400;color:var(--white)}
.listing{position:absolute;top:68px;width:150px;height:156px}
.listing-photo{width:150px;height:156px}
.listing-caption{position:absolute;left:12px;right:12px;bottom:14px;background:rgba(255,255,255,.92);text-align:center;padding:5px 4px;font-size:7px;line-height:10px;color:var(--text)}
.listing-caption strong{display:block;font-weight:600;color:var(--navy)}
.slider-dots{position:absolute;top:240px;left:0;width:100%;display:flex;justify-content:center;gap:6px}
.slider-dots span{width:6px;height:6px;border-radius:50%;background:rgba(255,255,255,.55)}
.slider-dots span.on{background:var(--white)}

.contact{position:absolute;top:905px;left:0;width:809px;height:161px;background:var(--light)}
.contact-map{position:absolute;left:0;top:0;width:405px;height:161px;background:linear-gradient(135deg,#e4e6e9,#cfd3d8)}
.contact-form{position:absolute;left:432px;top:0;width:290px}
.contact-form h2{font-size:13px;font-weight:400;color:#3a3f45;margin-top:22px;padding-bottom:7px;border-bottom:1px solid var(--line)}
.form-row{display:flex;gap:10px;margin-top:10px}
.field{flex:1;height:22px;background:var(--white);border:1px solid var(--line);font-size:7px;color:var(--muted);padding:6px 8px}
.submit{flex:1;height:22px;background:var(--footer);color:var(--white);font-size:7px;font-weight:700;text-align:center;padding-top:6px;letter-spacing:.5px}

.site-footer{position:absolute;top:1066px;left:0;width:809px;height:134px;background:var(--footer);color:var(--footer-text);font-size:7px}
.footer-info{position:absolute;top:37px;left:95px;right:95px;display:flex;align-items:center;justify-content:space-between}
.info-item{display:flex;align-items:center;gap:6px}
.social{display:flex;gap:8px}
.social span{width:9px;height:9px;border-radius:50%;background:var(--footer-text)}
.footer-rule{position:absolute;top:68px;left:0;width:809px;border-top:1px solid #3f4348}
.footer-links{position:absolute;top:80px;width:100%;text-align:center;letter-spacing:.3px}
.copyright{position:absolute;top:104px;width:100%;text-align:center;font-size:6.5px;color:#7f848a}
</style>
</head>
<body>

<header class="site-header">
  <div class="brand"><span class="brand-mark"></span><span class="brand-name">Brightmoor Crest</span></div>
  <nav class="main-nav">
    <a class="active" href="#">Home</a><a href="#">Services</a><a href="#">Listings</a><a href="#">About us</a><a href="#">Contact us</a>
  </nav>
</header>

<section class="hero" role="img" aria-label="Modern two-storey house with a pool and lounge chairs at dusk">
  <svg class="hero-arrow prev" viewBox="0 0 14 20"><path d="M11 2 3 10l8 8" fill="none" stroke="#fff" stroke-width="2"/></svg>
  <svg class="hero-arrow next" viewBox="0 0 14 20"><path d="M3 2l8 8-8 8" fill="none" stroke="#fff" stroke-width="2"/></svg>
</section>

<section class="welcome">
  <h1>Welcome to Brightmoor Crest Properties</h1>
  <p>Brightmoor Crest Properties helps homeowners and renters across the Texas Panhandle find the right place to live. We manage quality residential rentals today and are growing into multi-family, commercial and vacation properties. Our team handles listings, showings, leasing and maintenance so every owner and tenant enjoys a simple, reliable experience from the first visit to the final signature.</p>
</section>

<section class="services">
  <div class="service">
    <div class="service-icon"><svg width="22" height="22" viewBox="0 0 22 22"><path d="M3 11 11 4l8 7v8h-5v-5H8v5H3z" fill="#fff"/></svg></div>
    <h3>Residential Rental</h3>
    <p>Well kept single family homes for rent in quiet Amarillo neighborhoods, ready to move in.</p>
  </div>
  <div class="service">
    <div class="service-icon"><svg width="22" height="22" viewBox="0 0 22 22"><path d="M4 19V6h6v13zM12 19V3h6v16z" fill="#fff"/><path d="M6 8h2M6 11h2M6 14h2M14 6h2M14 9h2M14 12h2M14 15h2" stroke="#5b92d3" stroke-width="1.4"/></svg></div>
    <h3>Multi-Family Rentals</h3>
    <p>Duplexes and apartment buildings with flexible leases for growing households and investors.</p>
  </div>
  <div class="service">
    <div class="service-icon"><svg width="22" height="22" viewBox="0 0 22 22"><path d="M3 19V8h16v11zM6 8V4h10v4" fill="#fff"/><path d="M9 19v-5h4v5" fill="#5b92d3"/></svg></div>
    <h3>Commercial Rental</h3>
    <p>Office, retail and warehouse spaces in prime locations for local businesses of every size.</p>
  </div>
  <div class="service">
    <div class="service-icon"><svg width="22" height="22" viewBox="0 0 22 22"><rect x="3" y="7" width="16" height="12" rx="2" fill="#fff"/><path d="M8 7V4h6v3" fill="none" stroke="#fff" stroke-width="1.8"/></svg></div>
    <h3>Vacation Rental</h3>
    <p>Furnished getaway homes for short stays, weekend trips and family vacations all year.</p>
  </div>
</section>

<section class="listings">
  <h2>Our Real Estate Listings</h2>
  <article class="listing" style="left:89px">
    <div class="listing-photo" role="img" aria-label="White modern family home under a blue sky" style="background:linear-gradient(180deg,#8fb4de,#e8ecef 55%,#b8b2a6)"></div>
    <div class="listing-caption"><strong>Modern Family Home</strong>3 Beds 2 Baths</div>
  </article>
  <article class="listing" style="left:249px">
    <div class="listing-photo" role="img" aria-label="Row of cream townhouses on a sunny street" style="background:linear-gradient(180deg,#6f9fd4,#e3d6b8 50%,#8e8a7c)"></div>
    <div class="listing-caption"><strong>Downtown Townhouse</strong>2 Beds 2 Baths</div>
  </article>
  <article class="listing" style="left:409px">
    <div class="listing-photo" role="img" aria-label="White multi-storey office building" style="background:linear-gradient(180deg,#5d95d6,#f0f2f4 50%,#b9c3cc)"></div>
    <div class="listing-caption"><strong>Office Building</strong>12,000 Sq Ft</div>
  </article>
  <article class="listing" style="left:569px">
    <div class="listing-photo" role="img" aria-label="Vacation villa with palm trees" style="background:linear-gradient(180deg,#4f8bd2,#9fbf8a 50%,#e6dcc8)"></div>
    <div class="listing-caption"><strong>Palm Vacation Villa</strong>4 Beds 3 Baths</div>
  </article>
  <div class="slider-dots"><span class="on"></span><span></span><span></span><span></span></div>
</section>

<section class="contact">
  <div class="contact-map" role="img" aria-label="Faint grey map of the office location"></div>
  <form class="contact-form">
    <h2>Contact Us</h2>
    <div class="form-row"><div class="field">First Name</div><div class="field">Last Name</div></div>
    <div class="form-row"><div class="field">Phone</div><div class="field">Email</div></div>
    <div class="form-row"><div class="field">City</div><div class="submit">SUBMIT</div></div>
  </form>
</section>

<footer class="site-footer">
  <div class="footer-info">
    <div class="info-item"><svg width="9" height="11" viewBox="0 0 9 11"><path d="M4.5 11S0 6.5 0 4.5a4.5 4.5 0 0 1 9 0C9 6.5 4.5 11 4.5 11z" fill="#a9adb2"/><circle cx="4.5" cy="4.5" r="1.6" fill="#2f3236"/></svg>1420 Brightmoor Lane, Amarillo, TX 79101</div>
    <div class="info-item"><svg width="10" height="10" viewBox="0 0 10 10"><path d="M2 0h2l1 3-1.5 1a6 6 0 0 0 2.5 2.5L7 5l3 1v2a2 2 0 0 1-2 2A8 8 0 0 1 0 2a2 2 0 0 1 2-2z" fill="#a9adb2"/></svg>Tel/Fax: 806-555-0148</div>
    <div class="info-item"><svg width="11" height="8" viewBox="0 0 11 8"><rect width="11" height="8" fill="#a9adb2"/><path d="M0 0l5.5 4.5L11 0" fill="none" stroke="#2f3236"/></svg>Email: info@brightmoorcrest.com</div>
    <div class="social"><span></span><span></span><span></span><span></span></div>
  </div>
  <div class="footer-rule"></div>
  <div class="footer-links">Home &nbsp;|&nbsp; Services &nbsp;|&nbsp; Listings &nbsp;|&nbsp; About us &nbsp;|&nbsp; Contact us</div>
  <div class="copyright">Copyright © 2024 Brightmoor Crest Properties. All rights reserved.</div>
</footer>

</body>
</html>
```